Microsoft Word Template for 1, 2, and 4-page quick hit, topical pieces

I am looking for someone to create a professional and dynamic Microsoft Word Template that will allow us to easily add content to produce brochures and whitepapers on various topics. We'd like the template to be 4 pages with the idea that we may use all or just 1-2 of the pages in a brochure. We are fond of bold color, white space, and a good ratio of text to graphics. We have a large catalog of stock images so placeholders for photographs can be included if it fits the design. There is the possibility of expanded design opportunities in the future. I have attached our logo and colors.

Target Market(s)

Libraries - Public, Government, Higher Education, and Corporate

Font styles to use
Serif
Sans Serif

Requirements
Must have
• Editable Word Template that has 4 variable but cohesively designed pages. Use our logo and colors (see uploaded documents)
Nice to have
• Lots of white space, spaces for photos and graphics, spaces for blocks of text. Color.
Should not have
• Giant blocks of text. The exact same frame (header and footer) on each page.

```html
<!DOCTYPE html>
<html lang="en">
<head>
<meta charset="utf-8">
<title>Lumenfold Brochure Template – Four Pages</title>
<link href="https://fonts.googleapis.com/css2?family=Montserrat:wght@700;800&family=Lato:wght@300;400&display=swap" rel="stylesheet">
<style>
  :root {
    --backdrop: #4a494b;
    --paper: #ffffff;
    --maroon: #7d0026;
    --lime: #c3cf1c;
    --lime-deep: #8e9a12;
    --yellow: #e2e81e;
    --ink: #1d1d1d;
    --brown: #6b4a2a;
    --frame: #e9e79a;
  }
  * { box-sizing: border-box; margin: 0; padding: 0; }
  html, body { width: 1200px; height: 1200px; overflow: hidden; background: var(--backdrop); }
  .canvas { position: relative; width: 1200px; height: 1200px; font-family: "Lato", Arial, sans-serif; color: var(--ink); }
  .page { position: absolute; background: var(--paper); overflow: hidden; }
  .page--cover { left: 158px; top: 90px; width: 370px; height: 518px; }
  .page--intro { left: 672px; top: 90px; width: 370px; height: 518px; }
  .page--features { left: 162px; top: 629px; width: 368px; height: 516px; }
  .page--contact { left: 670px; top: 629px; width: 371px; height: 520px; }

  .footer-rule { position: absolute; left: 0; right: 0; height: 3px; background: var(--maroon); bottom: 12px; }
  .corner { position: absolute; right: 0; bottom: 0; width: 60px; height: 60px; }

  .brand { position: absolute; display: flex; align-items: center; gap: 8px; font-family: "Lato", Arial, sans-serif; font-weight: 300; color: var(--brown); }
  .brand__dot { border-radius: 50%; border: 3px solid var(--lime-deep); }

  /* cover */
  .cover__brand { left: 54px; top: 42px; font-size: 42px; letter-spacing: -0.5px; }
  .cover__brand .brand__dot { width: 46px; height: 46px; }
  .cover__photo { position: absolute; left: 0; top: 234px; width: 100%; height: 284px;
    background: linear-gradient(160deg, #9aa71a 0%, #6d7812 45%, #3f4508 100%); }
  .cover__badge { position: absolute; left: 68px; top: 120px; width: 228px; height: 228px; border-radius: 50%;
    background: var(--maroon); color: #fff; text-align: center; padding-top: 80px; }
  .cover__title { font-family: "Montserrat", Arial, sans-serif; font-weight: 700; font-size: 23px; letter-spacing: 0.5px; }
  .cover__lead { font-size: 12.4px; line-height: 14px; margin-top: 6px; padding: 0 20px; }

  /* intro */
  .intro__photo { position: absolute; left: 0; top: 0; width: 100%; height: 153px;
    background: linear-gradient(180deg, #b9cf10 0%, #cfd81c 55%, #a6b414 72%, #c4cf1a 100%); }
  .section-title { font-family: "Montserrat", Arial, sans-serif; font-weight: 800; color: var(--maroon); letter-spacing: 0.6px; }
  .intro__title { position: absolute; left: 34px; top: 120px; font-size: 19px; }
  .intro__body { position: absolute; left: 34px; width: 292px; font-size: 6.5px; line-height: 8.7px; }
  .intro__body--1 { top: 182px; }
  .intro__body--2 { top: 343px; }
  .intro__body--3 { top: 419px; }

  /* features */
  .features__title { position: absolute; left: 0; right: 0; top: 28px; text-align: center; font-size: 17px; }
  .feature { position: absolute; width: 163px; height: 185px; border: 1px solid var(--frame); text-align: center; }
  .feature--a { left: 18px; top: 70px; }
  .feature--b { left: 188px; top: 70px; }
  .feature--c { left: 18px; top: 263px; }
  .feature--d { left: 188px; top: 263px; }
  .feature__icon { display: block; margin: 14px auto 0; width: 70px; height: 70px; }
  .feature__name { font-family: "Montserrat", Arial, sans-serif; font-weight: 800; color: var(--maroon); font-size: 10.5px; margin-top: 10px; letter-spacing: 0.3px; }
  .feature__text { font-size: 6.4px; line-height: 8.6px; text-align: left; padding: 8px 10px 0 10px; }

  /* contact */
  .contact__photo { position: absolute; inset: 0;
    background: linear-gradient(170deg, #d6e21a 0%, #e6ea22 40%, #cdd718 70%, #e0e620 100%); }
  .contact__title { position: absolute; left: 24px; top: 50px; font-size: 17px; }
  .contact__lead { position: absolute; left: 24px; top: 79px; width: 335px; font-size: 6.6px; line-height: 8.7px; }
  .contact__list { position: absolute; left: 32px; top: 446px; list-style: none; font-size: 6.6px; line-height: 10.8px; }
  .contact__list li { display: flex; align-items: flex-start; gap: 4px; }
  .contact__list svg { width: 7px; height: 7px; margin-top: 2px; flex: none; }
  .contact__brand { left: 236px; top: 467px; font-size: 18px; gap: 5px; }
  .contact__brand .brand__dot { width: 16px; height: 16px; border-width: 2px; border-color: #d97a26; }
</style>
</head>
<body>
<main class="canvas">

  <!-- Page 1: cover -->
  <section class="page page--cover">
    <div class="brand cover__brand"><span class="brand__dot"></span>Lumenfold</div>
    <div class="cover__photo" role="img" aria-label="Photo of modern glass office towers at dusk, tinted lime green"></div>
    <div class="cover__badge">
      <h1 class="cover__title">LOREM IPSUM</h1>
      <p class="cover__lead">eiusmod tempor incididunt ut labore et dolore magna aliqua eiusmod tempor incididunt labore et</p>
    </div>
    <div class="footer-rule"></div>
    <svg class="corner" viewBox="0 0 60 60"><polygon points="60,0 60,60 0,60" fill="var(--maroon)"/></svg>
  </section>

  <!-- Page 2: introduction -->
  <section class="page page--intro">
    <div class="intro__photo" role="img" aria-label="City skyline photo across water, tinted lime green"></div>
    <h2 class="section-title intro__title">INTRODUCTION</h2>
    <p class="intro__body intro__body--1">Lorem ipsum dolor sit amet, consectetur adipiscing elit, sed do eiusmod tempor incididunt ut labore et dolore magna aliqua. Ut enim ad minim veniam, quis nostrud exercitation ullamco laboris nisi ut aliquip ex ea commodo consequat. Duis aute irure dolor in reprehenderit in voluptate velit esse cillum dolore eu fugiat nulla pariatur. Excepteur sint occaecat cupidatat non proident, sunt in culpa qui officia deserunt mollit anim id est laborum. Lorem ipsum dolor sit amet, consectetur adipiscing elit, sed do eiusmod tempor incididunt ut labore et dolore magna aliqua. Ut enim ad minim veniam, quis nostrud exercitation ullamco laboris nisi ut aliquip ex ea commodo consequat. Duis aute irure dolor in reprehenderit in voluptate velit esse cillum dolore eu fugiat nulla pariatur. Excepteur sint occaecat cupidatat non proident, sunt in culpa qui officia deserunt mollit anim id est laborum. Lorem ipsum dolor sit amet, consectetur adipiscing elit, sed do eiusmod tempor incididunt ut labore et dolore magna aliqua. Ut enim ad minim veniam, quis nostrud exercitation ullamco laboris nisi ut aliquip ex ea commodo consequat. Duis aute irure dolor in reprehenderit in voluptate velit esse cillum dolore eu fugiat nulla pariatur. Excepteur sint occaecat cupidatat non proident, sunt in culpa qui officia deserunt mollit anim id est laborum.</p>
    <p class="intro__body intro__body--2">Lorem ipsum dolor sit amet, consectetur adipiscing elit, sed do eiusmod tempor incididunt ut labore et dolore magna aliqua. Ut enim ad minim veniam, quis nostrud exercitation ullamco laboris nisi ut aliquip ex ea commodo consequat. Duis aute irure dolor in reprehenderit in voluptate velit esse cillum dolore eu fugiat nulla pariatur. Excepteur sint occaecat cupidatat non proident, sunt in culpa qui officia deserunt mollit anim id est laborum.</p>
    <p class="intro__body intro__body--3">Lorem ipsum dolor sit amet, consectetur adipiscing elit, sed do eiusmod tempor incididunt ut labore et dolore magna aliqua. Ut enim ad minim veniam, quis nostrud exercitation ullamco laboris nisi ut aliquip ex ea commodo consequat. Duis aute irure dolor in reprehenderit in voluptate velit esse cillum dolore eu fugiat nulla pariatur. Excepteur sint occaecat cupidatat non proident, sunt in culpa qui officia deserunt mollit anim id est laborum.</p>
    <div class="footer-rule"></div>
    <svg class="corner" viewBox="0 0 60 60"><polygon points="60,0 60,60 0,60" fill="var(--maroon)"/></svg>
  </section>

  <!-- Page 3: features -->
  <section class="page page--features">
    <h2 class="section-title features__title">OUR FEATURES</h2>

    <article class="feature feature--a">
      <svg class="feature__icon" viewBox="0 0 70 70">
        <circle cx="35" cy="35" r="35" fill="var(--maroon)"/>
        <g fill="none" stroke="var(--yellow)" stroke-width="2.2">
          <ellipse cx="35" cy="35" rx="22" ry="9"/>
          <ellipse cx="35" cy="35" rx="22" ry="9" transform="rotate(60 35 35)"/>
          <ellipse cx="35" cy="35" rx="22" ry="9" transform="rotate(-60 35 35)"/>
          <circle cx="35" cy="35" r="9"/>
        </g>
        <path d="M35 40 l-5-5 a3 3 0 0 1 5-4 a3 3 0 0 1 5 4 z" fill="var(--yellow)"/>
      </svg>
      <h3 class="feature__name">LOREM IPSUM</h3>
      <p class="feature__text">Lorem ipsum dolor sit amet, consectetur adipiscing elit, sed do eiusmod tempor incididunt ut labore et dolore magna aliqua. Ut enim ad minim veniam, quis nostrud exercitation ullamco laboris nisi ut aliquip ex ea commodo consequat. Duis aute irure dolor in reprehenderit in voluptate velit esse cillum</p>
    </article>

    <article class="feature feature--b">
      <svg class="feature__icon" viewBox="0 0 70 70">
        <circle cx="35" cy="35" r="35" fill="var(--maroon)"/>
        <g fill="none" stroke="var(--yellow)" stroke-width="2.2" stroke-linejoin="round">
          <rect x="20" y="22" width="30" height="20" rx="2"/>
          <path d="M13 45 h44 l-3 4 h-38 z"/>
        </g>
      </svg>
      <h3 class="feature__name">LOREM IPSUM</h3>
      <p class="feature__text">Lorem ipsum dolor sit amet, consectetur adipiscing elit, sed do eiusmod tempor incididunt ut labore et dolore magna aliqua. Ut enim ad minim veniam, quis nostrud exercitation ullamco laboris nisi ut aliquip ex ea commodo consequat. Duis aute irure dolor in reprehenderit in voluptate velit esse cillum</p>
    </article>

    <article class="feature feature--c">
      <svg class="feature__icon" viewBox="0 0 70 70">
        <circle cx="35" cy="35" r="35" fill="var(--maroon)"/>
        <g fill="none" stroke="var(--yellow)" stroke-width="2.6" stroke-linecap="round">
          <path d="M18 38 v-5 a17 17 0 0 1 34 0 v5"/>
          <path d="M50 44 q0 8 -12 9"/>
        </g>
        <rect x="15" y="34" width="7" height="13" rx="3" fill="var(--yellow)"/>
        <rect x="48" y="34" width="7" height="13" rx="3" fill="var(--yellow)"/>
        <rect x="32" y="50" width="7" height="5" rx="2" fill="var(--yellow)"/>
      </svg>
      <h3 class="feature__name">LOREM IPSUM</h3>
      <p class="feature__text">Lorem ipsum dolor sit amet, consectetur adipiscing elit, sed do eiusmod tempor incididunt ut labore et dolore magna aliqua. Ut enim ad minim veniam, quis nostrud exercitation ullamco laboris nisi ut aliquip ex ea commodo consequat. Duis aute irure dolor in reprehenderit in voluptate velit esse cillum</p>
    </article>

    <article class="feature feature--d">
      <svg class="feature__icon" viewBox="0 0 70 70">
        <circle cx="35" cy="35" r="35" fill="var(--maroon)"/>
        <g fill="none" stroke="var(--yellow)" stroke-width="2" stroke-linejoin="round">
          <rect x="30" y="20" width="20" height="14" rx="1.5"/>
          <rect x="16" y="30" width="22" height="15" rx="1.5"/>
          <path d="M27 45 v5 M21 51 h12 M40 34 v4"/>
          <path d="M30 14 h8 v6" stroke-dasharray="2 2"/>
          <circle cx="27" cy="37" r="4"/>
        </g>
      </svg>
      <h3 class="feature__name">LOREM IPSUM</h3>
      <p class="feature__text">Lorem ipsum dolor sit amet, consectetur adipiscing elit, sed do eiusmod tempor incididunt ut labore et dolore magna aliqua. Ut enim ad minim veniam, quis nostrud exercitation ullamco laboris nisi ut aliquip ex ea commodo consequat. Duis aute irure dolor in reprehenderit in voluptate velit esse cillum</p>
    </article>

    <div class="footer-rule"></div>
    <svg class="corner" viewBox="0 0 60 60"><polygon points="60,0 60,60 0,60" fill="var(--maroon)"/></svg>
  </section>

  <!-- Page 4: contact -->
  <section class="page page--contact">
    <div class="contact__photo" role="img" aria-label="Photo of business people walking through a bright glass lobby, tinted yellow"></div>
    <h2 class="section-title contact__title">CONTACT US</h2>
    <p class="contact__lead">Lorem ipsum dolor sit amet, consectetur adipiscing elit, sed do eiusmod tempor incididunt ut labore et dolore magna aliqua. Ut enim ad minim veniam, quis nostrud exercitation ullamco laboris nisi ut aliquip ex ea commodo consequat. Duis aute irure dolor in reprehenderit in voluptate velit esse cillum dolore eu fugiat nulla pariatur. Excepteur sint occaecat cupidatat non proident, sunt in culpa qui officia deserunt mollit anim id est laborum.</p>
    <ul class="contact__list">
      <li><svg viewBox="0 0 10 10"><path d="M5 10 L1.5 5 A3.8 3.8 0 1 1 8.5 5 Z" fill="var(--maroon)"/><circle cx="5" cy="3.6" r="1.3" fill="var(--yellow)"/></svg><span>134,Lorem ipsum dolor sit amet, consectetur<br>adipiscing elit, sed do</span></li>
      <li><svg viewBox="0 0 10 10"><circle cx="5" cy="5" r="4.5" fill="none" stroke="var(--maroon)" stroke-width="1.2"/><path d="M3.5 3 l1 1 -0.5 0.8 q0.6 1.2 1.4 1.6 l0.7-0.5 1 1 -0.8 0.8 q-2.5-0.6 -3.6-3.4z" fill="var(--maroon)"/></svg><span>123 456 7890</span></li>
      <li><svg viewBox="0 0 10 10"><rect x="0.5" y="2" width="9" height="6" fill="var(--maroon)"/><path d="M0.5 2 L5 5.5 L9.5 2" fill="none" stroke="var(--yellow)" stroke-width="0.8"/></svg><span>hello@lumenfold.com</span></li>
      <li><svg viewBox="0 0 10 10"><circle cx="5" cy="5" r="4.5" fill="var(--maroon)"/><path d="M0.5 5 h9 M5 0.5 q-3 4.5 0 9 M5 0.5 q3 4.5 0 9" fill="none" stroke="var(--yellow)" stroke-width="0.6"/></svg><span>www.lumenfold.com</span></li>
    </ul>
    <div class="brand contact__brand"><span class="brand__dot"></span>Lumenfold</div>
    <div class="footer-rule"></div>
    <svg class="corner" viewBox="0 0 60 60"><polygon points="60,0 60,60 0,60" fill="var(--maroon)"/></svg>
  </section>

</main>
</body>
</html>
```